Goat's Milk Soap

International product development company seeking designs for the following soap label:

Hand crafted in Mt Hollowbrook QLD Australia, Marren Valley
Second Generation Goat Farmers
Soap is hand made in appearance but gives an instant soothing feel when used
High in Vegetable oils and pure fresh goats milk (no powders used)
Give the emotional feel of Quality and Hand crafted
Label must stimulate an emotional response visually
Label must deliver to the customer anticipation for use.
Would anticipate that the label will be produced on a matte finish brown paper label or similar.

Logo should be no larger than 50mm x 50mm
Label should measure around 120mm x 70mm

It Company

```html
<!DOCTYPE html>
<html lang="en">
<head>
<meta charset="utf-8">
<title>Handmade Goat's Milk Soap Label</title>
<link rel="stylesheet" href="https://fonts.googleapis.com/css2?family=Pinyon+Script&family=Open+Sans:wght@400&display=swap">
<style>
  :root {
    --label-centre: #ffffff;
    --label-edge: #bccbd4;
    --ink: #15191b;
    --art-dark: #1a2224;
    --art-light: #c3d0d7;
  }
  html, body {
    margin: 0;
    padding: 0;
    overflow: hidden;
    background: var(--label-centre);
  }
  .label {
    position: relative;
    width: 1200px;
    height: 704px;
    overflow: hidden;
    background: radial-gradient(ellipse 62% 68% at 50% 46%, var(--label-centre) 0%, var(--label-centre) 22%, var(--label-edge) 100%);
  }
  .tagline {
    position: absolute;
    top: 10px;
    left: 0;
    width: 100%;
    margin: 0;
    text-align: center;
    font-family: "Pinyon Script", cursive;
    font-weight: 400;
    font-size: 68px;
    line-height: 1.2;
    color: var(--ink);
  }
  .hero-art {
    position: absolute;
    left: 411px;
    top: 127px;
    width: 378px;
    height: 313px;
  }
  .product-name {
    position: absolute;
    top: 462px;
    left: 0;
    width: 100%;
    margin: 0;
    text-align: center;
    font-family: "Pinyon Script", cursive;
    font-weight: 400;
    font-size: 122px;
    line-height: 1.2;
    color: var(--ink);
  }
  .origin {
    position: absolute;
    top: 645px;
    left: 0;
    width: 100%;
    margin: 0;
    text-align: center;
    font-family: "Open Sans", sans-serif;
    font-weight: 400;
    font-size: 29px;
    line-height: 1.3;
    color: var(--ink);
  }
</style>
</head>
<body>
  <main class="label">
    <p class="tagline">Handmade</p>

    <svg class="hero-art" viewBox="0 0 378 313" role="img" aria-label="Illustration area: silhouette of a woman blowing soap bubbles from her hand, rising from a cluster of bubbles with swirling flourishes">
      <defs>
        <linearGradient id="art-tone" x1="0" y1="0" x2="0" y2="1">
          <stop offset="0" stop-color="var(--art-dark)" stop-opacity="0.85"/>
          <stop offset="0.7" stop-color="var(--art-dark)" stop-opacity="0.6"/>
          <stop offset="1" stop-color="var(--art-light)"/>
        </linearGradient>
      </defs>
      <rect width="378" height="313" rx="18" fill="url(#art-tone)"/>
    </svg>

    <h1 class="product-name">Goat's Milk Soap</h1>

    <p class="origin">Mt Hollowbrook QLD Australia, Marren Valley</p>
  </main>
</body>
</html>
```